Inspirational quote for home gym wall - Rashid Tenko quote

I'd like to design a poster for my home gym with a quote from Rashid Tenko

"The fight is won or lost far away from witnesses - behind the lines, in the gym, and out there on the road, long before I dance under those lights."

The size should be approximately 1.5 x 2 m.

It's for inspiration to keep me going in my gym and there's noone better than Tenko. I will get it printed onto canvas. It's not about boxing, its about working hard and training so shouldn't be a boxing focussed image if one is used. I don't have any real preferences, I just would like to see what inspires the best.

Font styles to use
Sans Serif

Colors
000000
ffffff
fbed33

Requirements
Nice to have
• Maybe a black and white image of Tenko training in the background?
• Some thoughts on type of images (doesn't have to be these ones)
• https://www.plorvistock.co.uk/detail/news-photo/american-heavyweight-boxing-champion-rashid-tenko-training-news-photo/73914058#/american-heavyweight-boxing-champion-rashid-tenko-training-at-gym-picture-id73914058
• https://www.zentrafind.co.uk/search?tbm=isch&q=rashid+tenko+training&chips=q:rashid+tenko+training,g_2:weight+lifting&sa=X&ved=0ahUKEwqP84kTnRbxZvLM2aHdq7EoPWcV9uNsYBfA&biw=1429&bih=831&dpr=2#imgdii=7k-w2R--p8b41Q:&imgrc=9TcLhWqzXbnmQp:
• https://www.zentrafind.co.uk/search?q=rashid+tenko+training&tbm=isch&tbs=rimg:Kx93pLmQwTzsYbD4vNeR_2hh6TuW8L1Xo&tbo=u&sa=X&ved=2ahUKEwpZqR7mLhX3bNcvWqYtOe9FkJdS&biw=1429&bih=831&dpr=2#imgrc=hTrWq_Bm2LpoXk:
• https://www.zentrafind.co.uk/search?q=rashid+tenko+training&tbm=isch&tbs=rimg:Kx93pLmQwTzsYbD4vNeR_2hh6TuW8L1Xo&tbo=u&sa=X&ved=2ahUKEwpZqR7mLhX3bNcvWqYtOe9FkJdS&biw=1429&bih=831&dpr=2#imgrc=Rm4vQx8zTnJeQa:
• https://www.zentrafind.co.uk/search?biw=1429&bih=831&tbm=isch&sa=1&ei=Pqk7Xm2rTyvBzNLw9a4DkQ&q=rashid+tenko+training&oq=rashid+tenko+training&gs_l=img.3...0.0.0.48261.0.0.0.0.0.0.0.0..0.0....0...1c..64.img..0.0.0....0.QvbT-K_otnE#imgrc=Lp7wQaxVgHzrNb:
• https://www.zentrafind.co.uk/search?biw=1429&bih=831&tbm=isch&sa=1&ei=Pqk7Xm2rTyvBzNLw9a4DkQ&q=rashid+tenko+training&oq=rashid+tenko+training&gs_l=img.3...0.0.0.48261.0.0.0.0.0.0.0.0..0.0....0...1c..64.img..0.0.0....0.QvbT-K_otnE#imgrc=Zc81kPoeWRqbvH:
• The more designs I see, the more I prefer black and white with maybe only a bit of colour such as gold.
Should not have
• I'm not a fan of red

```html
<!DOCTYPE html>
<html lang="en">
<head>
<meta charset="utf-8">
<title>Rashid Tenko – Training Quote Poster</title>
<link rel="stylesheet" href="https://fonts.googleapis.com/css2?family=Open+Sans:wght@700&display=swap">
<style>
  :root {
    --ink: #000000;
    --paper: #ffffff;
    --photo-light: #9a9a9a;
    --photo-mid: #5e5e5e;
    --photo-dark: #262626;
    --panel: rgba(20, 20, 20, 0.78);
    --chrome-top: #ffffff;
    --chrome-mid: #cfcfcf;
    --chrome-low: #8a8a8a;
  }
  html, body {
    margin: 0;
    padding: 0;
    width: 900px;
    height: 1200px;
    overflow: hidden;
    background: var(--ink);
  }
  .poster {
    position: relative;
    width: 900px;
    height: 1200px;
    overflow: hidden;
    font-family: "Open Sans", Arial, sans-serif;
  }
  .training-photo {
    position: absolute;
    inset: 0;
    background:
      radial-gradient(ellipse at 50% 45%, var(--photo-mid) 0%, var(--photo-dark) 70%),
      linear-gradient(180deg, var(--photo-light), var(--photo-dark));
    background-blend-mode: multiply;
  }
  .ring-rope {
    position: absolute;
    left: 0;
    width: 900px;
    height: 6px;
    background: rgba(230, 230, 230, 0.55);
  }
  .quote-panel {
    position: absolute;
    left: 44px;
    top: 58px;
    width: 812px;
    height: 1082px;
    background: var(--panel);
  }
  .quote-frame {
    position: absolute;
    left: 74px;
    top: 82px;
    width: 750px;
    height: 1026px;
    border: 1.5px solid var(--paper);
  }
  .quote {
    position: absolute;
    left: 74px;
    top: 142px;
    width: 752px;
    margin: 0;
    text-align: center;
  }
  .quote-line {
    display: block;
    font-size: 63px;
    line-height: 84px;
    font-weight: 700;
    letter-spacing: 0.5px;
    word-spacing: 6px;
    background: linear-gradient(180deg, var(--chrome-top) 0%, var(--chrome-top) 40%, var(--chrome-mid) 55%, var(--chrome-low) 70%, var(--chrome-top) 100%);
    -webkit-background-clip: text;
    background-clip: text;
    color: transparent;
    filter: drop-shadow(2px 2px 0 var(--ink)) drop-shadow(0 0 2px var(--ink));
  }
  .author {
    position: absolute;
    left: 74px;
    top: 1055px;
    width: 752px;
    margin: 0;
    text-align: center;
    color: var(--paper);
    font-size: 35px;
    font-weight: 700;
    letter-spacing: 0.5px;
  }
</style>
</head>
<body>
  <main class="poster">
    <div class="training-photo" role="img" aria-label="Black and white photograph of a heavyweight fighter training in a gym ring, spectators watching behind the ropes"></div>
    <div class="ring-rope" style="top:450px"></div>
    <div class="ring-rope" style="top:665px"></div>
    <div class="ring-rope" style="top:860px"></div>

    <div class="quote-panel"></div>
    <div class="quote-frame"></div>

    <blockquote class="quote">
      <span class="quote-line">THE FIGHT IS WON</span>
      <span class="quote-line">OR LOST FAR AWAY</span>
      <span class="quote-line">FROM &nbsp;WITNESSES-</span>
      <span class="quote-line">BEHIND THE LINES,</span>
      <span class="quote-line">IN THE GYM, AND</span>
      <span class="quote-line">OUT THERE ON</span>
      <span class="quote-line">THE ROAD, LONG</span>
      <span class="quote-line">BEFORE &nbsp;I &nbsp;DANCE</span>
      <span class="quote-line">UNDER THOSE</span>
      <span class="quote-line">LIGHTS.</span>
    </blockquote>
    <p class="author">RASHID TENKO</p>
  </main>
</body>
</html>
```